I need a business Card Design for my practice , i am clinical herbalist. I am a herbalist specializing in Lyme disease, autism, autoimmune diseases, difficult to cure diseasesDifficult to cure diseases. In my innovative practice i link traditional medicine, herbs with science, immunologu ,pharmacology.

Industry/Entity Type

Business

Contact Information for Business Card

My company name : OŚRODEK ZIELNIK
My name : Piotr Kaleta
Name of my profession : Fitoterapeuta
In Polish language Fitoterapeuta is Herbalist .

e-mail: piotrkaleta@osrodekzielnik.com
www.osrodek-zielnik.pl
phone : 604 587 231
My company adress : Dąbrowa Sitnicka 41 , 38-415 Lużna
I dont have logo .

Requirements
Nice to have
• My company

```html
<!DOCTYPE html>
<html lang="pl">
<head>
<meta charset="utf-8">
<title>Ośrodek Zielnik – wizytówka</title>
<link rel="stylesheet" href="https://fonts.googleapis.com/css2?family=Open+Sans:wght@700&family=Roboto+Condensed:wght@700&family=Roboto:wght@400&display=swap">
<style>
  :root {
    --backdrop: #e7e4df;
    --card: #ffffff;
    --ink: #000000;
    --card-shadow: rgba(0, 0, 0, 0.18);
  }
  * { margin: 0; padding: 0; box-sizing: border-box; }
  html, body {
    width: 1200px;
    height: 1135px;
    overflow: hidden;
    background: var(--backdrop);
  }
  .canvas {
    position: relative;
    width: 1200px;
    height: 1135px;
  }
  .card {
    position: absolute;
    left: 235px;
    width: 679px;
    height: 405px;
    background: var(--card);
    box-shadow: 0 6px 18px var(--card-shadow);
    color: var(--ink);
  }
  .card--front { top: 90px; }
  .card--back { top: 625px; }

  .holder {
    position: absolute;
    left: 32px;
    top: 28px;
  }
  .holder__name {
    font-family: "Roboto Condensed", "Arial Narrow", sans-serif;
    font-weight: 700;
    font-size: 28px;
    line-height: 1;
  }
  .holder__role {
    margin-top: 6px;
    font-family: "Roboto", Arial, sans-serif;
    font-size: 12px;
    line-height: 1;
  }

  .company {
    font-family: "Open Sans", Arial, sans-serif;
    font-weight: 700;
    text-transform: uppercase;
    line-height: 1.15;
  }
  .company--front {
    position: absolute;
    right: 32px;
    top: 150px;
    font-size: 38px;
    text-align: right;
  }
  .company--back {
    position: absolute;
    left: 0;
    right: 0;
    top: 122px;
    font-size: 62px;
    line-height: 1.12;
    text-align: center;
  }

  .contact {
    position: absolute;
    left: 33px;
    top: 314px;
    list-style: none;
    font-family: "Roboto", Arial, sans-serif;
    font-size: 13.5px;
    line-height: 22.5px;
  }
  .contact__phone { letter-spacing: 1.5px; }
</style>
</head>
<body>
<main class="canvas">
  <section class="card card--front" aria-label="Przód wizytówki">
    <div class="holder">
      <h1 class="holder__name">Piotr Kaleta</h1>
      <p class="holder__role">Fitoterapeuta</p>
    </div>
    <p class="company company--front">Ośrodek<br>Zielnik</p>
    <ul class="contact">
      <li class="contact__phone">604 587 231</li>
      <li class="contact__email">piotrkaleta@osrodekzielnik.com</li>
      <li class="contact__web">www.osrodek-zielnik.pl</li>
    </ul>
  </section>

  <section class="card card--back" aria-label="Tył wizytówki">
    <p class="company company--back">Ośrodek<br>Zielnik</p>
  </section>
</main>
</body>
</html>
```